Bright Kestrel Studio - Redesign of our website - needs to be dynamic and alive!

We provide fun lessons exclusively in students' homes in music, art, yoga and acting. I like most of the graphics and copy on the site now, but it looks too static and there might be too much info to read on the home page. Needs movement, needs to generate excitement and be a fun place to visit, yet keeping professional-looking. The site needs better SEO, a better look and needs to generate more business, as several people see it each day but few contact us for details about our program. The site is brightkestrel-studio.test. I'd like it to continue to be hosted on my domain in Wordpress format so I can add and delete teacher photos from time to time. I like the way the teachers' bios currently pop up when a cursor is hovered over them on the Our Team page. Thank you and good luck!

Target Market(s)

Wealthy, college-educated households with children who live in the Greater Atlanta area

Industry/Entity Type

Education

Coding

Number of Pages Required

Requirements
Must have
• Home Page movement, excitement, but keeping it professional-looking. We're an educational company and want to market to people who are looking for a professional yet fun/exciting approach to lessons in their homes.
Nice to have
• The info on the Testimonials page can probably rotate and fade in/fade out on the home page or slide on/slide off instead of having a separate page for these.
• The info on the Trial Lessons page can probably be included as a banner on the home page too instead of being a separate page. Nice if I can change the text on this myself from time to time to mention any promotions I might be offering with regard to trial lessons.

```html
<!DOCTYPE html>
<html lang="en">
<head>
<meta charset="utf-8">
<title>Bright Kestrel Studio</title>
<link href="https://fonts.googleapis.com/css2?family=Open+Sans:wght@400;600;700&family=Roboto+Slab:wght@700&display=swap" rel="stylesheet">
<style>
:root{
  --orange:#f39a1e;
  --orange-dark:#e3841a;
  --purple:#5b2a86;
  --purple-dark:#4a1f70;
  --teal:#1aa3cf;
  --green:#8cc63f;
  --red:#e9572b;
  --ink:#333;
  --muted:#666;
  --blush:#fdf1ee;
  --line:#e6e6e6;
}
*{box-sizing:border-box;margin:0;padding:0}
html,body{width:1200px;height:3936px;overflow:hidden}
body{font-family:"Open Sans",Arial,sans-serif;color:var(--ink);background:#fff;font-size:15px;line-height:1.6}
.slab{font-family:"Roboto Slab",Georgia,serif}
.brand{font-family:"Open Sans",Arial,sans-serif;font-weight:700;color:var(--purple);font-size:30px;line-height:1.05;display:flex;align-items:center;gap:12px}
.brand .dot{width:22px;height:22px;border-radius:50%;background:var(--orange)}

/* header */
.topbar{height:144px;display:flex;align-items:center;justify-content:space-between;padding:0 96px;position:relative}
.topbar::before{content:"";position:absolute;left:0;right:0;top:0;height:6px;background:linear-gradient(90deg,var(--orange),var(--purple),var(--teal),var(--green))}
.top-right{display:flex;align-items:center;gap:18px}
.socials{display:flex;gap:8px}
.socials span{width:30px;height:30px;border-radius:50%;border:2px solid #bbb;display:block}
.mail-chip{display:flex;align-items:center;gap:8px;color:var(--orange);font-weight:600;font-size:14px}
.mail-chip .ico{width:30px;height:30px;border-radius:4px;background:var(--orange);display:flex;align-items:center;justify-content:center}
.phone-chip{display:flex;align-items:center;gap:8px;font-weight:700;color:var(--purple);font-size:16px}
.phone-chip .ico{width:34px;height:34px;border-radius:50%;border:2px solid var(--purple);display:flex;align-items:center;justify-content:center}
.nav{height:48px;background:var(--orange);display:flex;padding:0 96px;justify-content:space-between}
.nav a{color:#fff;text-decoration:none;font-size:14px;font-weight:600;line-height:48px;padding:0 18px}
.nav a.active{background:var(--purple)}

/* hero */
.hero{height:668px;position:relative;background:linear-gradient(180deg,#d8eef8,#eef8fc 70%,#fff);overflow:hidden}
.hero::before{content:"";position:absolute;inset:0;background:repeating-linear-gradient(90deg,rgba(255,255,255,.45) 0 40px,transparent 40px 80px)}
.hero-grass{position:absolute;left:0;right:0;bottom:0;height:70px;background:linear-gradient(180deg,#9ed36a,#6fb23b)}
.hero-copy{position:absolute;left:96px;top:170px;width:440px}
.hero-copy h1{font-size:56px;color:var(--purple);font-weight:700;line-height:1.1}
.hero-copy p{margin-top:18px;color:var(--muted);font-size:15px}
.btn{display:inline-block;background:var(--orange);color:#fff;font-weight:600;border-radius:22px;padding:9px 26px;font-size:14px}
.hero-copy .btn{margin-top:26px}
.dots{display:flex;gap:8px;margin-top:30px}
.dots i{width:12px;height:12px;border-radius:50%;border:2px solid var(--orange)}
.dots i:first-child{background:var(--orange)}
.hero-photo{position:absolute;right:96px;top:20px;width:500px;height:620px;border-radius:8px;background:radial-gradient(circle at 40% 45%,#d94b2b 0 18%,transparent 40%),radial-gradient(circle at 70% 55%,#c97d3d 0 15%,transparent 38%),linear-gradient(160deg,#f0c9a4,#e69a5a)}

/* sections */
.section-title{text-align:center;color:var(--purple);font-size:30px}
.section-title::after{content:"";display:block;width:60px;height:3px;background:var(--orange);margin:14px auto 0}

.courses{height:580px;padding-top:40px}
.courses .intro{width:840px;margin:26px auto 0;text-align:center;color:var(--muted);font-size:14px}
.cards{display:flex;gap:16px;justify-content:center;margin-top:34px}
.card{width:220px;height:356px;color:#fff;position:relative;border-radius:4px}
.card .head{height:170px;display:flex;flex-direction:column;align-items:center;justify-content:center;gap:14px}
.card .ic{width:72px;height:72px;border-radius:50%;background:rgba(255,255,255,.25);display:flex;align-items:center;justify-content:center}
.card h3{font-size:18px;font-weight:700}
.card .body{height:186px;padding:16px 20px;font-size:12.5px;text-align:center;line-height:1.5;background:rgba(0,0,0,.12)}
.card .plus{position:absolute;left:50%;bottom:-16px;transform:translateX(-50%);width:34px;height:34px;border-radius:50%;background:#fff;color:var(--ink);font-weight:700;text-align:center;line-height:34px;box-shadow:0 2px 6px rgba(0,0,0,.2)}
.c-orange{background:var(--red)}.c-teal{background:var(--teal)}.c-green{background:var(--green)}.c-purple{background:var(--purple)}

.programs{height:580px;background:var(--blush);position:relative;padding:56px 96px}
.programs h2{color:var(--purple);font-size:30px}
.programs h2::after{content:"";display:block;width:60px;height:3px;background:var(--orange);margin-top:12px}
.prog-list{margin-top:30px;width:560px}
.prog{display:flex;gap:18px;margin-bottom:22px}
.prog .ic{flex:none;width:34px;height:34px;border-radius:50%;background:var(--orange);display:flex;align-items:center;justify-content:center}
.prog h4{color:var(--orange);font-size:16px;font-weight:700}
.prog p{font-size:13px;color:var(--muted);line-height:1.5}
.prog-photo{position:absolute;right:96px;top:40px;width:440px;height:540px;background:linear-gradient(160deg,#f6e3d4,#f4a24c 60%,#ef8a24)}

.gallery{height:640px;padding-top:44px}
.grid{width:1008px;margin:40px auto 0;display:grid;grid-template-columns:260px 330px 400px;grid-template-rows:220px 220px;gap:9px}
.grid div{border-radius:2px}
.g1{background:linear-gradient(140deg,#3a4a5a,#7a8f6a)}
.g2{background:linear-gradient(140deg,#6d4a35,#c59a6b)}
.g3{background:linear-gradient(140deg,#3c2a2a,#a15c3c)}
.g4{background:linear-gradient(140deg,#1d1d2a,#5c6a7a)}
.g5{background:linear-gradient(140deg,#4a3a30,#8a6a50)}
.g6{background:linear-gradient(140deg,#2a2a30,#b07a5a)}

.testimonials{height:480px;padding-top:36px}
.tcols{display:flex;gap:40px;justify-content:center;margin-top:30px}
.tcol{width:300px}
.avatar{width:120px;height:120px;border-radius:50%;border:5px solid #eee;margin:0 auto;background:linear-gradient(160deg,#e8c9a8,#b88a6a)}
.quote{color:var(--orange);font-size:40px;line-height:1;margin-top:14px;font-family:Georgia,serif}
.tcol p{font-size:13px;color:var(--muted);line-height:1.5}
.tcol.hl p{background:var(--red);color:#fff;padding:10px 12px}
.tcol .src{display:block;margin-top:14px;color:var(--orange);font-weight:700;font-size:14px;border-bottom:1px solid var(--line);padding-bottom:6px}

.trial{height:380px;background:linear-gradient(135deg,var(--purple),var(--purple-dark));position:relative;color:#fff;padding:70px 96px 0 320px}
.trial-art{position:absolute;left:120px;top:24px;width:140px;height:330px;background:linear-gradient(180deg,#e7b36b,#8fd0ea 60%,#3f6b9a)}
.trial h2{font-size:30px;color:#fff}
.trial p{margin-top:14px;font-size:14px;width:740px;opacity:.92}
.trial .call{margin-top:22px;font-size:20px;font-weight:600}

.footer{height:340px;padding:46px 96px 0;display:flex;gap:60px;background:#fafafa}
.footer .brand{width:210px;align-self:flex-start;margin-top:40px}
.fcol h5{color:var(--orange);font-size:15px;font-weight:700;margin-bottom:14px}
.fcol ul{list-style:none;font-size:13px;line-height:2}
.fcol li::before{content:"› ";color:var(--orange)}
.contact-row{display:flex;gap:10px;font-size:13px;margin-bottom:14px}
.contact-row .ic{flex:none;width:26px;height:26px;border-radius:50%;background:var(--orange);display:flex;align-items:center;justify-content:center}
.form{width:300px}
.form .row{display:flex;gap:8px;margin-bottom:8px}
.form .field{flex:1;height:30px;border:1px solid #ddd;background:#fff;font-size:12px;color:#999;padding:5px 8px}
.form .area{height:66px}
.form .btn{border-radius:3px;font-size:12px;padding:6px 16px;background:var(--red)}
.copy{height:76px;background:#eee;display:flex;align-items:center;justify-content:space-between;padding:0 96px;font-size:13px;color:var(--muted)}
.copy .socials span{border-color:#999}
</style>
</head>
<body>

<header class="topbar">
  <div class="brand"><span class="dot"></span>Bright Kestrel<br>Studio</div>
  <div class="top-right">
    <div class="socials"><span></span><span></span><span></span><span></span></div>
    <div class="mail-chip"><span class="ico"><svg width="16" height="12" viewBox="0 0 16 12"><rect x="1" y="1" width="14" height="10" fill="none" stroke="#fff" stroke-width="1.6"/><path d="M1 1l7 6 7-6" fill="none" stroke="#fff" stroke-width="1.6"/></svg></span>hello@brightkestrel-studio.test</div>
    <div class="phone-chip"><span class="ico"><svg width="14" height="14" viewBox="0 0 24 24"><path d="M6 2l4 4-2 3c1 3 4 6 7 7l3-2 4 4-3 4C10 22 2 14 2 5z" fill="#5b2a86"/></svg></span>(555) 013-4780</div>
  </div>
</header>
<nav class="nav">
  <a class="active">Home</a><a>About Us</a><a>Courses</a><a>Programs</a><a>Our Team</a><a>Trial Lessons</a><a>Gallery</a><a>Testimonials</a><a>Contact Us</a>
</nav>

<section class="hero">
  <div class="hero-photo" role="img" aria-label="Two children playing acoustic and electric guitars"></div>
  <div class="hero-copy">
    <h1 class="slab">Bright Kestrel Studio</h1>
    <p>Greater Atlanta's best piano, guitar, voice, art lessons and more, all taught in your home.</p>
    <span class="btn">Trial Lessons</span>
    <div class="dots"><i></i><i></i><i></i><i></i><i></i></div>
  </div>
  <div class="hero-grass"></div>
</section>

<section class="courses">
  <h2 class="section-title slab">Courses We Offer</h2>
  <p class="intro">Learning to play a musical instrument should be an enjoyable journey, not a chore. We exclusively offer in-home, individual music lessons for most instruments including piano, guitar, voice, drums, woodwinds, strings and many more using the unique Bright Kestrel Method. In addition to teaching the foundations of reading music we will help you play the styles of music and songs you are excited to learn!</p>
  <div class="cards">
    <div class="card c-orange"><div class="head"><span class="ic"><svg width="34" height="34" viewBox="0 0 24 24"><path d="M9 18V5l11-2v13" fill="none" stroke="#fff" stroke-width="2"/><circle cx="6" cy="18" r="3" fill="#fff"/><circle cx="17" cy="16" r="3" fill="#fff"/></svg></span><h3>Music Lessons</h3></div><div class="body">Private lessons in a wide range of instruments, tailored to each student and taught by skilled teachers who make every week in your home fun.</div><span class="plus">+</span></div>
    <div class="card c-teal"><div class="head"><span class="ic"><svg width="34" height="34" viewBox="0 0 24 24"><circle cx="12" cy="12" r="9" fill="none" stroke="#fff" stroke-width="2"/><circle cx="9" cy="10" r="1.3" fill="#fff"/><circle cx="15" cy="10" r="1.3" fill="#fff"/><path d="M8 14q4 4 8 0" fill="none" stroke="#fff" stroke-width="2"/></svg></span><h3>Acting Lessons</h3></div><div class="body">Stage and screen coaching that builds confidence, voice and presence, with scenes and monologues chosen to match each student's goals.</div><span class="plus">+</span></div>
    <div class="card c-green"><div class="head"><span class="ic"><svg width="34" height="34" viewBox="0 0 24 24"><path d="M4 20l4-1 11-11-3-3L5 16z" fill="#fff"/></svg></span><h3>Visual Art Lessons</h3></div><div class="body">Drawing, painting and mixed media lessons that guide young artists through new techniques while letting their own style grow.</div><span class="plus">+</span></div>
    <div class="card c-purple"><div class="head"><span class="ic"><svg width="34" height="34" viewBox="0 0 24 24"><circle cx="12" cy="5" r="2.2" fill="#fff"/><path d="M4 11h16M12 8v7l-4 6M12 15l4 6" fill="none" stroke="#fff" stroke-width="2"/></svg></span><h3>Yoga Classes</h3></div><div class="body">Gentle yoga sessions for children and families that improve focus, balance and calm, all from the comfort of your living room.</div><span class="plus">+</span></div>
  </div>
</section>

<section class="programs">
  <h2 class="slab">Our Programs</h2>
  <div class="prog-list">
    <div class="prog"><span class="ic"><svg width="16" height="16" viewBox="0 0 24 24"><path d="M4 12l5 5L20 6" fill="none" stroke="#fff" stroke-width="3"/></svg></span><div><h4>Fall Spring Program:</h4><p>This is our primary program, made of 30 weekly lessons offered between September and May. Students who enroll find it brings real results.</p></div></div>
    <div class="prog"><span class="ic"><svg width="16" height="16" viewBox="0 0 24 24"><path d="M4 12l5 5L20 6" fill="none" stroke="#fff" stroke-width="3"/></svg></span><div><h4>10 Session Workshops:</h4><p>All workshops in theater, music, visual arts and yoga are offered in 10 session packages which are renewable upon completion.</p></div></div>
    <div class="prog"><span class="ic"><svg width="16" height="16" viewBox="0 0 24 24"><path d="M4 12l5 5L20 6" fill="none" stroke="#fff" stroke-width="3"/></svg></span><div><h4>Summer Session:</h4><p>Summer is a great time to try lessons in a new subject or to continue the progress that began during the previous season.</p></div></div>
    <div class="prog"><span class="ic"><svg width="16" height="16" viewBox="0 0 24 24"><path d="M4 12l5 5L20 6" fill="none" stroke="#fff" stroke-width="3"/></svg></span><div><h4>Trial Lessons:</h4><p>The first two lessons are considered trial lessons, helping you decide if our program and the instructor are exactly right for your needs.</p></div></div>
  </div>
  <div class="prog-photo" role="img" aria-label="Young girl in orange top singing into a microphone"></div>
</section>

<section class="gallery">
  <h2 class="section-title slab">Our Gallery</h2>
  <div class="grid">
    <div class="g1" role="img" aria-label="Student at a music lesson"></div>
    <div class="g2" role="img" aria-label="Teacher guiding a young guitarist"></div>
    <div class="g3" role="img" aria-label="Students playing drums in a studio"></div>
    <div class="g4" role="img" aria-label="Child playing a keyboard"></div>
    <div class="g5" role="img" aria-label="Drum kit lesson in a home"></div>
    <div class="g6" role="img" aria-label="Group of students at an art session"></div>
  </div>
</section>

<section class="testimonials">
  <h2 class="section-title slab">Our Testimonials</h2>
  <div class="tcols">
    <div class="tcol"><div class="avatar" role="img" aria-label="Portrait of a parent reviewer"></div><div class="quote">“</div><p>"I can't say enough about how wonderful I think the studio's program is. Our teacher makes learning fun and my son now looks forward to each week."</p><span class="src">- Reviewpost.test Review</span></div>
    <div class="tcol hl"><div class="avatar" role="img" aria-label="Portrait of a parent reviewer"></div><div class="quote">“</div><p>"They were very patient, matched my child with a teacher who fits perfectly, and the progress after only a few months has been amazing to see."</p><span class="src">- Reviewpost.test Review</span></div>
    <div class="tcol"><div class="avatar" role="img" aria-label="Portrait of a parent reviewer"></div><div class="quote">“</div><p>"I really enjoy the convenience of having someone come to my home. It works perfectly for our family and I would recommend them to anyone."</p><span class="src">- Reviewpost.test Review</span></div>
  </div>
</section>

<section class="trial">
  <div class="trial-art" role="img" aria-label="Illustrated musician playing a saxophone"></div>
  <h2 class="slab">Trial Lessons</h2>
  <p>Why not take a trial lesson or two and see what the Bright Kestrel Studio experience is all about? Try a lesson with one of our teachers in your home, and then decide if our program is right for you.</p>
  <div class="call">Call us at (555) 013-4780 or e-mail us to arrange your first lesson.</div>
</section>

<footer class="footer">
  <div class="brand"><span class="dot"></span>Bright Kestrel<br>Studio</div>
  <div class="fcol"><h5>QUICK LINKS</h5><ul><li>Home</li><li>Courses</li><li>About Us</li><li>Programs</li><li>Our Team</li><li>Contact Us</li></ul></div>
  <div class="fcol"><h5>CONTACT US</h5>
    <div class="contact-row"><span class="ic"><svg width="12" height="14" viewBox="0 0 24 28"><path d="M12 0a9 9 0 0 0-9 9c0 7 9 19 9 19s9-12 9-19a9 9 0 0 0-9-9z" fill="#fff"/></svg></span><div><b>Address:</b><br>120 Maple Grove Ln<br>Fairview, GA 30000</div></div>
    <div class="contact-row"><span class="ic"><svg width="12" height="12" viewBox="0 0 24 24"><path d="M6 2l4 4-2 3c1 3 4 6 7 7l3-2 4 4-3 4C10 22 2 14 2 5z" fill="#fff"/></svg></span><div><b>Phone:</b><br>(555) 013-4780</div></div>
    <div class="contact-row"><span class="ic"><svg width="12" height="10" viewBox="0 0 16 12"><rect x="1" y="1" width="14" height="10" fill="none" stroke="#fff" stroke-width="2"/></svg></span><div><b>Mail:</b><br>hello@brightkestrel-studio.test</div></div>
  </div>
  <div class="fcol form"><h5>CONTACT FORM</h5>
    <div class="row"><span class="field">Name</span><span class="field">Phone</span></div>
    <div class="row"><span class="field">Email</span></div>
    <div class="row"><span class="field area">Message</span></div>
    <span class="btn">SEND MESSAGE</span>
  </div>
</footer>
<div class="copy"><span>Copyright © 2017 Bright Kestrel Studio. All Rights Reserved.</span><div class="socials"><span></span><span></span><span></span><span></span></div></div>

</body>
</html>
```